PDF-Dokumente für Vermietung und Verwaltung von Immobilien
Zielgruppe
WohnKranich, Vermietung und Verwaltung von Immoblien
Aufgabenstellung
Wir haben ganz viele Dokumente, die als PDF erstellt werden sollen, Einheitlich im CI Design, mit Logo etc. Manche PDFS müssen ausfüllbar sein andere sind einfach nur zum Drucken. es sind ca 10-20 Word/PDF Dokumente.

```html
<!DOCTYPE html>
<html lang="de">
<head>
<meta charset="utf-8">
<title>WohnKranich – Dokumentvorlagen</title>
<link href="https://fonts.googleapis.com/css2?family=Encode+Sans+Condensed:wght@400;600;700&family=Didact+Gothic&family=Tinos&display=swap" rel="stylesheet">
<style>
:root{
  --navy:#1d2c5e;
  --orange:#f07d22;
  --green:#3a9a3c;
  --field:#dde6fb;
  --row:#ececec;
  --ink:#222;
  --paper:#fff;
}
*{box-sizing:border-box;margin:0;padding:0}
html,body{width:800px;height:1200px;overflow:hidden;background:var(--paper)}
.sheet{position:relative;width:800px;height:1200px}
.page{position:absolute;width:343px;height:485px;border:1px solid #555;background:var(--paper);overflow:hidden;
  font-family:"Encode Sans Condensed",sans-serif;color:var(--navy)}
.p1{left:40px;top:52px}.p2{left:417px;top:49px}.p3{left:40px;top:600px}.p4{left:417px;top:596px}
.abs{position:absolute;white-space:nowrap}

/* letterhead */
.brand{position:absolute;top:44px;left:0;width:100%;text-align:center;font-family:"Encode Sans Condensed",sans-serif;
  font-weight:600;font-size:10px;letter-spacing:.4px;color:var(--navy)}
.brand-square{display:inline-block;width:8px;height:8px;background:var(--navy);margin-right:4px;vertical-align:-1px}
.partner-badge{position:absolute;left:236px;top:74px;width:76px;height:37px;background:var(--navy);border-radius:0 0 6px 0}

/* intro */
.title{left:40px;top:126px;font-weight:700;font-size:7.2px}
.step{left:40px;font-size:5.2px}
.step a{color:var(--navy);text-decoration:underline}
.note{left:40px;font-size:3.9px;line-height:5.3px;font-weight:600;white-space:normal;width:250px}
.tip{left:42px;font-size:4.1px;font-weight:600}
.dot{display:inline-block;width:7px;height:7px;border-radius:50%;background:var(--orange);vertical-align:middle;margin-right:2px}
.section{left:38px;top:223px;font-weight:700;font-size:5.8px;text-decoration:underline}
.section .dot{margin-left:2px}
.lbl{font-size:5.2px}
.strong{font-weight:700}
.field{position:absolute;height:7px;border-bottom:.6px solid var(--navy);font-family:"Tinos",serif;font-size:5px;color:#222;line-height:7px;padding-left:1px;white-space:nowrap;overflow:hidden}
.filled .field{background:var(--field)}
.box{display:inline-block;width:5px;height:5px;border:.6px solid #444;vertical-align:-1px;margin-right:3px;font-size:5px;line-height:4px;text-align:center;color:var(--navy)}
.box.on::after{content:"✓"}
.ital{font-style:italic}

/* footer band */
.band{position:absolute;left:0;bottom:0;width:100%;height:5px;background:var(--navy)}
.band::after{content:"";position:absolute;left:262px;top:0;width:2px;height:5px;background:var(--paper);transform:skewX(-20deg)}
.filled .band{bottom:1.5px}
.filled .band-accent{position:absolute;left:0;bottom:0;width:100%;height:1.5px;background:var(--green)}

/* checklist */
.cl-title{position:absolute;top:76px;width:100%;text-align:center;font-family:"Didact Gothic",sans-serif;font-size:7.5px;color:#111}
.cl-head{position:absolute;left:34px;top:95px;width:277px;height:13px;background:var(--green);color:#fff;font-family:"Didact Gothic",sans-serif;
  font-size:6px;display:flex;align-items:center}
.cl-head span{padding-left:5px;width:138px}
.cl-head span+span{border-left:.6px solid #fff}
.cl-group{position:absolute;left:34px;font-family:"Didact Gothic",sans-serif;font-size:4.2px;font-weight:700;color:#111}
.cl-table{position:absolute;left:34px;width:277px;border-collapse:collapse;table-layout:fixed;font-family:"Didact Gothic",sans-serif;font-size:3.8px;color:#111}
.cl-table td{height:10.6px;border:.6px solid #333;background:var(--row);padding:0 3px;line-height:4px;vertical-align:middle}
.cl-table col.a{width:138px}.cl-table col.b{width:105px}.cl-table col.c{width:34px}
.cl-table td.chk{text-align:center;font-size:6px;color:var(--navy)}
.cl-table td.chk::before{content:"";display:inline-block;width:7px;height:7px;background:#f8f8fb;vertical-align:middle}
.cl-table td.chk.on::before{display:none}
.sendnote{position:absolute;left:35px;top:435px;width:92px;height:33px;border:.6px solid #333;font-family:"Didact Gothic",sans-serif;
  font-style:italic;font-size:4px;line-height:6px;text-align:center;padding-top:6px;color:#111}
.sign{position:absolute;left:152px;top:452px;font-family:"Didact Gothic",sans-serif;font-size:4.6px;color:#111}
.sign-x{position:absolute;left:192px;top:455px;font-size:8px;color:#111;font-family:"Didact Gothic",sans-serif}
.sign-line{position:absolute;left:190px;top:465px;width:100px;height:.6px;background:#333}
.sign-field{position:absolute;left:199px;top:445px;width:107px;height:20px;background:var(--field);font-family:"Tinos",serif;font-size:4.8px;line-height:20px;padding-left:2px;color:#222}
</style>
</head>
<body>
<div class="sheet">

<!-- Formular leer -->
<section class="page p1 form">
  <div class="brand"><span class="brand-square"></span>WohnKranich</div>
  <div class="partner-badge" role="img" aria-label="Partnerplakette Hauswert-Portal"></div>

  <div class="abs title">Immobilienbewertung leicht gemacht.</div>
  <div class="abs step" style="top:140px">1.&nbsp;&nbsp; Füllen Sie einfach diesen Fragebogen bei der Hausbesichtigung aus.</div>
  <div class="abs step" style="top:152px">2.&nbsp;&nbsp; Geben Sie die Kriterien unter <a>www.hauswert-portal.de/anfrage</a> ein.</div>
  <div class="abs step" style="top:164px">3.&nbsp;&nbsp; Nach den Zahlungsmodalitäten erhalten Sie sofort Ihre Immobilienbewertung im PDF-Format.</div>
  <div class="abs note" style="top:177px">Hinweis: Im Folgenden finden Sie eine Checkliste aller Dinge, die für eine Hausbesichtigung beachtenswert sind. Trotz des umfangreichen Fragenkatalogs übernehmen wir keine Haftung für dessen Vollständigkeit und weisen darauf hin, dass es wertbeeinflussende Merkmale am Objekt geben kann, die hier nicht enthalten sind.</div>
  <div class="abs tip" style="top:197px"><span class="dot"></span>Tipp: Die orange markierten Punkte sind für eine Online-Immobilienbewertung wichtig.</div>

  <div class="abs section">Basisinformationen<span class="dot"></span></div>
  <div class="abs lbl strong" style="left:38px;top:238px">Anschrift</div>
  <div class="abs lbl" style="left:38px;top:247px">Straße, Hausnr.</div>
  <div class="abs lbl" style="left:38px;top:256px">Postleitzahl, Ort</div>
  <div class="field" style="left:103px;top:245px;width:91px"></div>
  <div class="field" style="left:103px;top:254px;width:91px"></div>
  <div class="abs lbl strong" style="left:198px;top:247px">Besichtigt am:</div>
  <div class="abs lbl strong" style="left:198px;top:256px">Angebotspreis:</div>
  <div class="field" style="left:243px;top:245px;width:32px"></div>
  <div class="field" style="left:243px;top:254px;width:32px"></div>
  <div class="abs lbl strong" style="left:278px;top:256px">€</div>

  <div class="abs lbl strong" style="left:38px;top:275px">Eigentümer</div>
  <div class="abs lbl" style="left:38px;top:284px">Name</div>
  <div class="abs lbl" style="left:38px;top:293px">Telefon</div>
  <div class="abs lbl" style="left:38px;top:302px">Gründe Verkauf</div>
  <div class="field" style="left:103px;top:282px;width:66px"></div>
  <div class="field" style="left:103px;top:291px;width:66px"></div>
  <div class="field" style="left:103px;top:300px;width:66px"></div>
  <div class="abs lbl strong" style="left:171px;top:275px">Makler</div>
  <div class="abs lbl" style="left:171px;top:284px">Name</div>
  <div class="abs lbl" style="left:171px;top:293px">Telefon</div>
  <div class="abs lbl" style="left:171px;top:302px">E-Mail</div>
  <div class="field" style="left:235px;top:282px;width:67px"></div>
  <div class="field" style="left:235px;top:291px;width:67px"></div>
  <div class="field" style="left:235px;top:300px;width:67px"></div>

  <div class="abs lbl" style="left:38px;top:322px">Baujahr</div>
  <div class="abs lbl" style="left:38px;top:331px">Wohnfläche</div>
  <div class="abs lbl" style="left:38px;top:340px">Grundstücksfläche</div>
  <div class="abs lbl" style="left:38px;top:349px">Balkon</div>
  <div class="abs lbl" style="left:38px;top:358px">Terrasse</div>
  <div class="abs lbl" style="left:38px;top:367px">(Tief)Garage/Carport</div>
  <div class="field" style="left:115px;top:320px;width:20px"></div>
  <div class="field" style="left:115px;top:329px;width:20px"></div><div class="abs lbl" style="left:137px;top:331px">m²</div>
  <div class="field" style="left:115px;top:338px;width:20px"></div><div class="abs lbl" style="left:137px;top:340px">m²</div>
  <div class="field" style="left:115px;top:347px;width:20px"></div><div class="abs lbl" style="left:137px;top:349px">m²</div>
  <div class="field" style="left:115px;top:356px;width:20px"></div><div class="abs lbl" style="left:137px;top:358px">m²</div>
  <div class="field" style="left:115px;top:365px;width:10px"></div><div class="abs lbl" style="left:128px;top:367px">(Anzahl)</div>

  <div class="abs lbl" style="left:173px;top:322px"><span class="box"></span>Das Objekt ist vermietet?</div>
  <div class="abs lbl ital" style="left:185px;top:331px"><span class="box"></span>Mietvertrag vorhanden</div>
  <div class="abs lbl" style="left:173px;top:340px"><span class="box"></span>Erschließungskosten bezahlt</div>
  <div class="abs lbl" style="left:181px;top:349px">(Wasser-/Stromanschluss etc.)</div>
  <div class="abs lbl" style="left:173px;top:358px"><span class="box"></span>Weitere Erschließung geplant/erforderlich</div>
  <div class="abs lbl" style="left:173px;top:367px"><span class="box"></span>Unterkellert</div>

  <div class="band"></div>
</section>

<!-- Formular ausgefüllt -->
<section class="page p2 form filled">
  <div class="brand"><span class="brand-square"></span>WohnKranich</div>
  <div class="partner-badge" role="img" aria-label="Partnerplakette Hauswert-Portal"></div>

  <div class="abs title">Immobilienbewertung leicht gemacht.</div>
  <div class="abs step" style="top:140px">1.&nbsp;&nbsp; Füllen Sie einfach diesen Fragebogen bei der Hausbesichtigung aus.</div>
  <div class="abs step" style="top:152px">2.&nbsp;&nbsp; Geben Sie die Kriterien unter <a>www.hauswert-portal.de/anfrage</a> ein.</div>
  <div class="abs step" style="top:164px">3.&nbsp;&nbsp; Nach den Zahlungsmodalitäten erhalten Sie sofort Ihre Immobilienbewertung im PDF-Format.</div>
  <div class="abs note" style="top:177px">Hinweis: Im Folgenden finden Sie eine Checkliste aller Dinge, die für eine Hausbesichtigung beachtenswert sind. Trotz des umfangreichen Fragenkatalogs übernehmen wir keine Haftung für dessen Vollständigkeit und weisen darauf hin, dass es wertbeeinflussende Merkmale am Objekt geben kann, die hier nicht enthalten sind.</div>
  <div class="abs tip" style="top:197px"><span class="dot"></span>Tipp: Die orange markierten Punkte sind für eine Online-Immobilienbewertung wichtig.</div>

  <div class="abs section">Basisinformationen<span class="dot"></span></div>
  <div class="abs lbl strong" style="left:38px;top:238px">Anschrift</div>
  <div class="abs lbl" style="left:38px;top:247px">Straße, Hausnr.</div>
  <div class="abs lbl" style="left:38px;top:256px">Postleitzahl, Ort</div>
  <div class="field" style="left:103px;top:245px;width:91px">Musterstraße 123</div>
  <div class="field" style="left:103px;top:254px;width:91px">00000 Musterstadt</div>
  <div class="abs lbl strong" style="left:198px;top:247px">Besichtigt am:</div>
  <div class="abs lbl strong" style="left:198px;top:256px">Angebotspreis:</div>
  <div class="field" style="left:243px;top:245px;width:46px">00/00/2024</div>
  <div class="field" style="left:243px;top:254px;width:46px">000000 <span style="color:#9aa">€</span></div>

  <div class="abs lbl strong" style="left:38px;top:275px">Eigentümer</div>
  <div class="abs lbl" style="left:38px;top:284px">Name</div>
  <div class="abs lbl" style="left:38px;top:293px">Telefon</div>
  <div class="abs lbl" style="left:38px;top:302px">Gründe Verkauf</div>
  <div class="field" style="left:103px;top:282px;width:66px">Mustermann</div>
  <div class="field" style="left:103px;top:291px;width:66px">01234567888</div>
  <div class="field" style="left:103px;top:300px;width:66px">dfghjklpöäü</div>
  <div class="abs lbl strong" style="left:171px;top:275px">Makler</div>
  <div class="abs lbl" style="left:171px;top:284px">Name</div>
  <div class="abs lbl" style="left:171px;top:293px">Telefon</div>
  <div class="abs lbl" style="left:171px;top:302px">E-Mail</div>
  <div class="field" style="left:225px;top:282px;width:79px">Musterfrau</div>
  <div class="field" style="left:225px;top:291px;width:79px">012345678900</div>
  <div class="field" style="left:225px;top:300px;width:79px"></div>

  <div class="abs lbl" style="left:38px;top:322px">Baujahr</div>
  <div class="abs lbl" style="left:38px;top:331px">Wohnfläche</div>
  <div class="abs lbl" style="left:38px;top:340px">Grundstücksfläche</div>
  <div class="abs lbl" style="left:38px;top:349px">Balkon</div>
  <div class="abs lbl" style="left:38px;top:358px">Terrasse</div>
  <div class="abs lbl" style="left:38px;top:367px">(Tief)Garage/Carport</div>
  <div class="field" style="left:115px;top:320px;width:22px">0000</div>
  <div class="field" style="left:115px;top:329px;width:22px">000</div><div class="abs lbl" style="left:138px;top:331px">m²</div>
  <div class="field" style="left:115px;top:338px;width:22px">0000</div><div class="abs lbl" style="left:138px;top:340px">m²</div>
  <div class="field" style="left:115px;top:347px;width:22px">00</div><div class="abs lbl" style="left:138px;top:349px">m²</div>
  <div class="field" style="left:115px;top:356px;width:22px">00</div><div class="abs lbl" style="left:138px;top:358px">m²</div>
  <div class="field" style="left:115px;top:365px;width:8px">2</div><div class="abs lbl" style="left:128px;top:367px">(Anzahl)</div>

  <div class="abs lbl" style="left:173px;top:322px"><span class="box on"></span>Das Objekt ist vermietet?</div>
  <div class="abs lbl ital" style="left:185px;top:331px"><span class="box on"></span>Mietvertrag vorhanden</div>
  <div class="abs lbl" style="left:173px;top:340px"><span class="box"></span>Erschließungskosten bezahlt</div>
  <div class="abs lbl" style="left:181px;top:349px">(Wasser-/Stromanschluss etc.)</div>
  <div class="abs lbl" style="left:173px;top:358px"><span class="box on"></span>Weitere Erschließung geplant/erforderlich</div>
  <div class="abs lbl" style="left:173px;top:367px"><span class="box"></span>Unterkellert</div>

  <div class="band"></div><div class="band-accent"></div>
</section>

<!-- Checkliste leer -->
<section class="page p3 checklist">
  <div class="brand"><span class="brand-square"></span>WohnKranich</div>
  <div class="cl-title">Checkliste Unterlagen</div>
  <div class="cl-head"><span>Was wird für ein Gutachten benötigt ?</span><span>Woher bekomme ich die Unterlagen ?</span></div>

  <div class="cl-group" style="top:123px">Bauunterlagen und Genehmigungen</div>
  <table class="cl-table" style="top:132px"><colgroup><col class="a"><col class="b"><col class="c"></colgroup>
    <tr><td>Grundbuchauszug</td><td>Grundbuchamt (Amtsgericht)</td><td class="chk"></td></tr>
    <tr><td>Flurkarte (Lageplan)</td><td>Katasteramt (Bauamt)</td><td class="chk"></td></tr>
    <tr><td>Baulastenauskunft</td><td>Baulastenverzeichnis (Bauamt)</td><td class="chk"></td></tr>
    <tr><td>Wohnflächen- und Nutzflächenberechnung (Quadratmeter)</td><td>Genehmigte Baupläne, Bauakte (Bauamt)</td><td class="chk"></td></tr>
    <tr><td>Grundrisspläne von allen Geschossen (auch Keller)</td><td>Genehmigte Baupläne, Bauakte (Bauamt)</td><td class="chk"></td></tr>
    <tr><td>Schnitte von allen Geschossen</td><td>Genehmigte Baupläne, Bauakte (Bauamt)</td><td class="chk"></td></tr>
    <tr><td>Ansichten</td><td>Genehmigte Baupläne, Bauakte (Bauamt)</td><td class="chk"></td></tr>
    <tr><td>Schlussabnahmeschein (Bauabnahme)</td><td>Genehmigte Baupläne, Bauakte (Bauamt)</td><td class="chk"></td></tr>
    <tr><td>Bei Sanierung oder Anbau: Jahr und Kostenaufwand. Zusätzlich genehmigte Bauunterlagen und Schlussabnahmeschein</td><td>Genehmigte Baupläne, Bauakte (Bauamt)</td><td class="chk"></td></tr>
  </table>

  <div class="cl-group" style="top:241px">Bei Wohnungseigentum</div>
  <table class="cl-table" style="top:250px"><colgroup><col class="a"><col class="b"><col class="c"></colgroup>
    <tr><td>Teilungserklärung (bei Wohnungseigentum)</td><td>Verwalter/Grundakte (Grundbuchamt) alter Kaufvertrag</td><td class="chk"></td></tr>
    <tr><td>Bezeichnung des Wohnungseigentums (z.B. Whg. Nr. 5)</td><td>Teilungserklärung/Grundbuchauszug/alter Kaufvertrag/ Grundakte (Grundbuchamt)</td><td class="chk"></td></tr>
    <tr><td>Anschrift des Verwalters</td><td>Letzte Abrechnung</td><td class="chk"></td></tr>
    <tr><td>Aktuelles Hausgeld</td><td>Verwalter/Abrechnung</td><td class="chk"></td></tr>
    <tr><td>Die letzten 3 Protokolle der Versammlung</td><td>Verwalter/eigene Unterlagen</td><td class="chk"></td></tr>
    <tr><td>Energieausweis</td><td>Verwalter/eigene Unterlagen</td><td class="chk"></td></tr>
  </table>

  <div class="cl-group" style="top:326px">Bei Grundbuch eingetragene Rechte</div>
  <table class="cl-table" style="top:335px"><colgroup><col class="a"><col class="b"><col class="c"></colgroup>
    <tr><td>Zum Beispiel: Erbbaurecht / Wegerechte / Dienstbarkeiten / Leitungsrechte / Rentenrechte</td><td>Grundakte (Grundbuchamt) Ursprünglicher Notarvertrag in Ihren eigenen Unterlagen</td><td class="chk"></td></tr>
  </table>

  <div class="cl-group" style="top:358px">Sonstiges</div>
  <table class="cl-table" style="top:367px"><colgroup><col class="a"><col class="b"><col class="c"></colgroup>
    <tr><td>Bei vermieteten Objekten: Mietverträge und letztes Mieterhöhungsschreiben. Kontaktdaten der Mieter.</td><td>Aus Ihren Unterlagen</td><td class="chk"></td></tr>
    <tr><td>Energieausweis</td><td>Aus Ihren Unterlagen</td><td class="chk"></td></tr>
    <tr><td>Falls Sie als Betreuer durch das Gericht bestellt sind: Gerichtliche Bestellungsurkunde.</td><td>Aus Ihren Unterlagen</td><td class="chk"></td></tr>
    <tr><td>Vollmacht zu Akteneinsicht beim Bauamt und Grundbuchamt</td><td>Aus dem Auftrag als Vordruck</td><td class="chk"></td></tr>
    <tr><td>Mieteraufstellung (Mietverträge)</td><td>Aus Ihren Unterlagen</td><td class="chk"></td></tr>
  </table>

  <div class="sendnote">Bitte senden Sie uns die benötigten<br>Unterlagen möglichst vor dem<br>Ortstermin in Kopie zu.</div>
  <div class="sign">Ort; Datum:</div>
  <div class="sign-x">X</div>
  <div class="sign-line"></div>
  <div class="band"></div>
</section>

<!-- Checkliste ausgefüllt -->
<section class="page p4 checklist filled">
  <div class="brand"><span class="brand-square"></span>WohnKranich</div>
  <div class="cl-title">Checkliste Unterlagen</div>
  <div class="cl-head"><span>Was wird für ein Gutachten benötigt ?</span><span>Woher bekomme ich die Unterlagen ?</span></div>

  <div class="cl-group" style="top:123px">Bauunterlagen und Genehmigungen</div>
  <table class="cl-table" style="top:132px"><colgroup><col class="a"><col class="b"><col class="c"></colgroup>
    <tr><td>Grundbuchauszug</td><td>Grundbuchamt (Amtsgericht)</td><td class="chk on">✓</td></tr>
    <tr><td>Flurkarte (Lageplan)</td><td>Katasteramt (Bauamt)</td><td class="chk on">✓</td></tr>
    <tr><td>Baulastenauskunft</td><td>Baulastenverzeichnis (Bauamt)</td><td class="chk"></td></tr>
    <tr><td>Wohnflächen- und Nutzflächenberechnung (Quadratmeter)</td><td>Genehmigte Baupläne, Bauakte (Bauamt)</td><td class="chk"></td></tr>
    <tr><td>Grundrisspläne von allen Geschossen (auch Keller)</td><td>Genehmigte Baupläne, Bauakte (Bauamt)</td><td class="chk on">✓</td></tr>
    <tr><td>Schnitte von allen Geschossen</td><td>Genehmigte Baupläne, Bauakte (Bauamt)</td><td class="chk"></td></tr>
    <tr><td>Ansichten</td><td>Genehmigte Baupläne, Bauakte (Bauamt)</td><td class="chk on">✓</td></tr>
    <tr><td>Schlussabnahmeschein (Bauabnahme)</td><td>Genehmigte Baupläne, Bauakte (Bauamt)</td><td class="chk"></td></tr>
    <tr><td>Bei Sanierung oder Anbau: Jahr und Kostenaufwand. Zusätzlich genehmigte Bauunterlagen und Schlussabnahmeschein</td><td>Genehmigte Baupläne, Bauakte (Bauamt)</td><td class="chk"></td></tr>
  </table>

  <div class="cl-group" style="top:241px">Bei Wohnungseigentum</div>
  <table class="cl-table" style="top:250px"><colgroup><col class="a"><col class="b"><col class="c"></colgroup>
    <tr><td>Teilungserklärung (bei Wohnungseigentum)</td><td>Verwalter/Grundakte (Grundbuchamt) alter Kaufvertrag</td><td class="chk on">✓</td></tr>
    <tr><td>Bezeichnung des Wohnungseigentums (z.B. Whg. Nr. 5)</td><td>Teilungserklärung/Grundbuchauszug/alter Kaufvertrag/ Grundakte (Grundbuchamt)</td><td class="chk on">✓</td></tr>
    <tr><td>Anschrift des Verwalters</td><td>Letzte Abrechnung</td><td class="chk on">✓</td></tr>
    <tr><td>Aktuelles Hausgeld</td><td>Verwalter/Abrechnung</td><td class="chk"></td></tr>
    <tr><td>Die letzten 3 Protokolle der Versammlung</td><td>Verwalter/eigene Unterlagen</td><td class="chk"></td></tr>
    <tr><td>Energieausweis</td><td>Verwalter/eigene Unterlagen</td><td class="chk"></td></tr>
  </table>

  <div class="cl-group" style="top:326px">Bei Grundbuch eingetragene Rechte</div>
  <table class="cl-table" style="top:335px"><colgroup><col class="a"><col class="b"><col class="c"></colgroup>
    <tr><td>Zum Beispiel: Erbbaurecht / Wegerechte / Dienstbarkeiten / Leitungsrechte / Rentenrechte</td><td>Grundakte (Grundbuchamt) Ursprünglicher Notarvertrag in Ihren eigenen Unterlagen</td><td class="chk"></td></tr>
  </table>

  <div class="cl-group" style="top:358px">Sonstiges</div>
  <table class="cl-table" style="top:367px"><colgroup><col class="a"><col class="b"><col class="c"></colgroup>
    <tr><td>Bei vermieteten Objekten: Mietverträge und letztes Mieterhöhungsschreiben. Kontaktdaten der Mieter.</td><td>Aus Ihren Unterlagen</td><td class="chk"></td></tr>
    <tr><td>Energieausweis</td><td>Aus Ihren Unterlagen</td><td class="chk on">✓</td></tr>
    <tr><td>Falls Sie als Betreuer durch das Gericht bestellt sind: Gerichtliche Bestellungsurkunde.</td><td>Aus Ihren Unterlagen</td><td class="chk"></td></tr>
    <tr><td>Vollmacht zu Akteneinsicht beim Bauamt und Grundbuchamt</td><td>Aus dem Auftrag als Vordruck</td><td class="chk"></td></tr>
    <tr><td>Mieteraufstellung (Mietverträge)</td><td>Aus Ihren Unterlagen</td><td class="chk"></td></tr>
  </table>

  <div class="sendnote">Bitte senden Sie uns die benötigten<br>Unterlagen möglichst vor dem<br>Ortstermin in Kopie zu.</div>
  <div class="sign">Ort; Datum:</div>
  <div class="sign-field">Musterstadt, 30.08.2024</div>
  <div class="sign-x">X</div>
  <div class="sign-line"></div>
  <div class="band"></div><div class="band-accent"></div>
</section>

</div>
</body>
</html>
```